Business card design for Plumbing and Gas fitting company

We need a business card design for our plumbing and gas fitting company using the company logo and director details. Design should be modern and eye-catching however kept reasonably simple. This design should be targeted at commercial businesses/work so professionalism is key.

Target Market(s)

Commercial/business

Industry/Entity Type

Plumbing

Contact Information for Business Card

Warren Dohey
Director
027 581 9043
warren@vantorplumbingandgas.example
PO Box 7816
Palmerston North 4472

Font styles to use
Sans Serif

Requirements
Must have
• Logo
• Modern
• Kept simple
Nice to have
• Colour scheme based around logo

```html
<!DOCTYPE html>
<html lang="en">
<head>
<meta charset="utf-8">
<title>Vantor Plumbing &amp; Gas – Business Card</title>
<link href="https://fonts.googleapis.com/css2?family=Lato:wght@400;700;900&display=swap" rel="stylesheet">
<style>
  :root {
    --backdrop: #eceef0;
    --card: #f8f8f8;
    --brand-blue: #1a6fbf;
    --charcoal: #2e2e2f;
    --tab-grey: #dcdcdc;
    --ink: #222222;
    --ink-soft: #555555;
    --accent-orange: #e07a2e;
    --white: #ffffff;
  }
  * { box-sizing: border-box; margin: 0; padding: 0; }
  html, body {
    width: 1200px;
    height: 800px;
    overflow: hidden;
    background: var(--backdrop);
    font-family: "Lato", Arial, sans-serif;
  }
  .sheet {
    position: relative;
    width: 1200px;
    height: 800px;
    display: flex;
    align-items: center;
    justify-content: center;
    gap: 40px;
  }
  .card {
    position: relative;
    width: 540px;
    height: 309px;
    background: var(--card);
    border-radius: 4px;
    overflow: hidden;
    box-shadow: 0 10px 28px rgba(0, 0, 0, 0.12);
  }
  .card-shapes {
    position: absolute;
    inset: 0;
    width: 100%;
    height: 100%;
  }
  .brand {
    position: absolute;
    display: flex;
    align-items: center;
    gap: 10px;
    color: var(--brand-blue);
    font-weight: 900;
    white-space: nowrap;
  }
  .brand-dot {
    border-radius: 50%;
    background: var(--accent-orange);
    flex: none;
  }
  /* Back side */
  .card-back .brand {
    left: 0;
    right: 0;
    top: 130px;
    justify-content: center;
    font-size: 30px;
  }
  .card-back .brand-dot { width: 28px; height: 28px; }

  /* Front side */
  .card-front .brand {
    left: 34px;
    top: 140px;
    font-size: 21px;
  }
  .card-front .brand-dot { width: 20px; height: 20px; }

  .person {
    position: absolute;
    right: 56px;
    top: 38px;
    text-align: right;
    color: var(--ink);
  }
  .person-name {
    font-size: 19px;
    letter-spacing: 0.5px;
    text-transform: uppercase;
    font-weight: 400;
  }
  .person-name strong { font-weight: 900; }
  .person-role {
    font-size: 10px;
    letter-spacing: 1px;
    text-transform: uppercase;
    color: var(--ink-soft);
    margin-top: 1px;
  }
  .address {
    position: absolute;
    left: 300px;
    top: 146px;
    font-size: 12.5px;
    color: var(--white);
  }
  .contact-list {
    position: absolute;
    left: 284px;
    top: 192px;
    list-style: none;
    color: var(--white);
    font-size: 11.5px;
  }
  .contact-list li {
    display: flex;
    align-items: center;
    gap: 9px;
    margin-bottom: 12px;
  }
  .contact-icon {
    width: 18px;
    height: 18px;
    border-radius: 50%;
    background: var(--brand-blue);
    display: flex;
    align-items: center;
    justify-content: center;
    flex: none;
  }
  .contact-icon svg { width: 10px; height: 10px; }
</style>
</head>
<body>
<main class="sheet">

  <!-- Card back: brand side -->
  <section class="card card-back" aria-label="Business card, brand side">
    <svg class="card-shapes" viewBox="0 0 540 309" aria-hidden="true">
      <polygon points="0,0 540,0 540,30 84,30 52,62 0,62" fill="var(--brand-blue)"/>
      <polygon points="0,0 540,0 540,24 80,24 48,56 0,56" fill="var(--charcoal)"/>
      <polygon points="0,309 540,309 540,247 488,247 456,279 0,279" fill="var(--brand-blue)"/>
      <polygon points="0,309 540,309 540,253 492,253 460,285 0,285" fill="var(--charcoal)"/>
    </svg>
    <div class="brand">
      <span class="brand-name">Vantor Plumbing &amp; Gas</span>
      <span class="brand-dot"></span>
    </div>
  </section>

  <!-- Card front: contact side -->
  <section class="card card-front" aria-label="Business card, contact side">
    <svg class="card-shapes" viewBox="0 0 540 309" aria-hidden="true">
      <path d="M318,28 H540 V100 H318 A18,18 0 0 1 300,82 V46 A18,18 0 0 1 318,28 Z" fill="var(--tab-grey)"/>
      <path d="M520,18 H540 V86 H520 A12,12 0 0 1 508,74 V30 A12,12 0 0 1 520,18 Z" fill="var(--brand-blue)"/>
      <path d="M300,138 H540 V172 H285 V153 A15,15 0 0 1 300,138 Z" fill="var(--brand-blue)"/>
      <path d="M289,170 H540 V309 H265 V194 A24,24 0 0 1 289,170 Z" fill="var(--charcoal)"/>
      <rect x="0" y="236" width="265" height="73" fill="var(--brand-blue)"/>
    </svg>

    <div class="brand">
      <span class="brand-name">Vantor Plumbing &amp; Gas</span>
      <span class="brand-dot"></span>
    </div>

    <div class="person">
      <p class="person-name"><strong>Warren</strong> Dohey</p>
      <p class="person-role">Director</p>
    </div>

    <p class="address">PO Box 7816 Palmerston North 4472</p>

    <ul class="contact-list">
      <li>
        <span class="contact-icon">
          <svg viewBox="0 0 24 24" aria-hidden="true"><path fill="#fff" d="M6.6 10.8a15.1 15.1 0 0 0 6.6 6.6l2.2-2.2a1 1 0 0 1 1-.25 11.4 11.4 0 0 0 3.6.57 1 1 0 0 1 1 1V20a1 1 0 0 1-1 1A17 17 0 0 1 3 4a1 1 0 0 1 1-1h3.5a1 1 0 0 1 1 1c0 1.25.2 2.45.57 3.57a1 1 0 0 1-.25 1z"/></svg>
        </span>
        <span>027 581 9043</span>
      </li>
      <li>
        <span class="contact-icon">
          <svg viewBox="0 0 24 24" aria-hidden="true"><path fill="#fff" d="M3 5h18a1 1 0 0 1 1 1v12a1 1 0 0 1-1 1H3a1 1 0 0 1-1-1V6a1 1 0 0 1 1-1zm9 7.2L20 7H4z"/></svg>
        </span>
        <span>warren@vantorplumbingandgas.example</span>
      </li>
    </ul>
  </section>

</main>
</body>
</html>
```